Chestnut Farm Logo and Business Card

We need a new logo design and new business cards for a recently purchased mature Chestnut Farm in the south west of Southern Ridges, the farm is called Willowmere Glen, We will be adding value to the chestnuts by creating a range of chestnut products based on the fact that chestnuts are a healthy, gluten free product that is suited to the vegetarian market as well as the health food market. We will be selling the products through farmers markets, restaurants, health food stores and online. The final design should communicate a healthy modern down to earth image.
Updates

Sorry, I should have given the details for the business cards.

Address is 
Willowmere Glen
PO Box 417 
Bramblewood, Southern Ridges, 6318

Email is 
willowmere.glen@fernpost.com

Website is
www.glenhollowfoods.com

Phone number is 
(08) 9412 7730

Many thanks

We would like to see the logo separate to the business card as well if possible please?

Industry/Entity Type

Farm

Logo Text

Willowmere Glen

```html
<!DOCTYPE html>
<html lang="en">
<head>
<meta charset="utf-8">
<title>Willowmere Glen — Business Card</title>
<link href="https://fonts.googleapis.com/css2?family=Source+Sans+3:wght@400;700&display=swap" rel="stylesheet">
<style>
  :root {
    --page: #ffffff;
    --paper: #ecebe4;
    --paper-light: #f4f3ee;
    --leaf-green: #8cc63f;
    --leaf-green-dark: #7cb535;
    --earth-brown: #5c2a26;
    --earth-brown-dark: #4e2320;
    --cream: #ede6da;
    --address-green: #a9c04e;
  }
  html, body {
    margin: 0;
    padding: 0;
    width: 1200px;
    height: 1000px;
    overflow: hidden;
    background: var(--page);
  }
  .canvas {
    position: relative;
    width: 1200px;
    height: 1000px;
  }
  .business-card {
    position: absolute;
    left: 68px;
    top: 162px;
    width: 1063px;
    height: 649px;
    overflow: hidden;
    background: radial-gradient(ellipse at 30% 20%, var(--paper-light), var(--paper));
    font-family: "Source Sans 3", "Source Sans Pro", sans-serif;
  }
  .card-shapes {
    position: absolute;
    inset: 0;
  }
  .brand {
    position: absolute;
    right: 228px;
    top: 190px;
    display: flex;
    align-items: center;
    gap: 18px;
  }
  .brand-dot {
    width: 34px;
    height: 34px;
    border-radius: 50%;
    background: var(--leaf-green);
  }
  .brand-name {
    margin: 0;
    font-weight: 700;
    font-size: 64px;
    line-height: 1;
    color: var(--earth-brown);
    letter-spacing: 0.5px;
  }
  .contact {
    position: absolute;
    right: 230px;
    text-align: right;
    color: var(--cream);
    font-weight: 400;
    margin: 0;
    line-height: 1.2;
    white-space: nowrap;
    text-shadow: 5px 12px 0 rgba(30, 10, 8, 0.55);
  }
  .contact-phone { top: 352px; font-size: 42px; }
  .contact-email { top: 420px; font-size: 38px; }
  .postal-address {
    position: absolute;
    left: 146px;
    top: 566px;
    margin: 0;
    font-size: 38px;
    line-height: 1.2;
    color: var(--address-green);
    word-spacing: 2px;
    white-space: pre;
  }
</style>
</head>
<body>
<div class="canvas">
  <section class="business-card">
    <svg class="card-shapes" width="1063" height="649" viewBox="0 0 1063 649" aria-hidden="true">
      <defs>
        <linearGradient id="greenBand" x1="0" y1="0" x2="1" y2="1">
          <stop offset="0" stop-color="var(--leaf-green)"/>
          <stop offset="1" stop-color="var(--leaf-green-dark)"/>
        </linearGradient>
        <linearGradient id="brownSweep" x1="0" y1="0" x2="1" y2="1">
          <stop offset="0" stop-color="var(--earth-brown)"/>
          <stop offset="1" stop-color="var(--earth-brown-dark)"/>
        </linearGradient>
      </defs>
      <rect class="green-band" x="0" y="335" width="640" height="314" fill="url(#greenBand)"/>
      <path class="brown-sweep" d="M0,578 C230,420 560,310 880,306 C970,305 1030,310 1063,318 L1063,649 L0,649 Z" fill="url(#brownSweep)"/>
    </svg>

    <div class="brand">
      <span class="brand-dot"></span>
      <h1 class="brand-name">Willowmere Glen</h1>
    </div>

    <p class="contact contact-phone">(08) 9412 7730</p>
    <p class="contact contact-email">willowmere.glen@fernpost.com</p>

    <p class="postal-address">PO Box 417  Bramblewood  Southern Ridges  6318</p>
  </section>
</div>
</body>
</html>
```